Electronic call to action mailer

I am launching my new web site and would like to send an electronic mailer to a segmented base. The base would be mostly mothers with children and I want them to shop at my new web site.

I would like to include a call to action - if they register as members they will get 20% off their first purchase and a 10% thereafter as members.

They will also be in a lucky draw contest for a $500 voucher to use at our wen site.
Updates

I have updated the details I require. As this is a call to action page, it should be really catchy that we brand new company that promises to bring quality children's products to them. The company's vision is pinned to producing and distributing organic products and products that are produced with fair trade practices.

Reason: I was late in updating my brief and I think there are a few designs that I already like. I just need to have the updates in

Target Market(s)

Parents that are interested in quality products for kids

Industry/Entity Type

Electronic

Font styles to use
Sans Serif

Colors
c1b2d3
86cfc6
f04a50

Requirements
Must have
• I page that is really easy to get the message. 5 consolation prizes that will be from the Tiny Amber Meadows toiletry range. (picture included). Winner gets $500 worth of goods (at RRP)
Must mention that this is in conjunction with the launch of our new on-line shop.
Must mention that our range of clothes are new to Singapore and we have exclusivity with the brands
terms and conditions apply
Nice to have
• A catchy tag line, making them want to become a member

```html
<!DOCTYPE html>
<html lang="en">
<head>
<meta charset="utf-8">
<title>Soft Sprout – Member Launch Mailer</title>
<link rel="stylesheet" href="https://fonts.googleapis.com/css2?family=Roboto:wght@400;700;900&family=Roboto+Condensed:wght@400;700&display=swap">
<style>
  :root {
    --board: #d9d9da;
    --cyan: #2cbcd2;
    --cyan-deep: #1aa9c1;
    --yellow: #fff200;
    --red: #e8313f;
    --red-deep: #c9202c;
    --lavender: #c1b2d3;
    --lavender-light: #d6cce3;
    --lavender-deep: #a99bc6;
    --purple: #6f67b0;
    --ink: #2d2d3a;
    --navy: #253858;
    --white: #ffffff;
    --teal: #86cfc6;
  }
  * { box-sizing: border-box; margin: 0; padding: 0; }
  html, body { width: 1200px; height: 850px; overflow: hidden; }
  body {
    background: var(--board);
    font-family: "Roboto", Arial, sans-serif;
    position: relative;
  }
  .flyer {
    position: absolute;
    top: 110px;
    width: 450px;
    height: 636px;
    overflow: hidden;
    background: var(--white);
    box-shadow: 0 6px 10px rgba(0,0,0,0.18);
  }
  .flyer--a { left: 112px; }
  .flyer--b { left: 623px; }
  .flyer > * { position: absolute; }

  .header-band { left: 0; top: 0; width: 100%; height: 127px; background: var(--cyan); }
  .flyer--b .header-band { height: 150px; }
  .header-curve { left: 0; top: 100px; width: 100%; height: 60px; }

  .body-field {
    left: 0; top: 292px; width: 100%; bottom: 0;
    background: radial-gradient(circle at 28% 22%, var(--lavender-light) 0%, var(--lavender) 45%, var(--lavender-deep) 100%);
  }
  .flyer--b .body-field { top: 352px; }

  .member-tag {
    left: 137px; top: 1px; width: 248px; height: 23px;
    background: var(--yellow);
    color: var(--ink);
    font-size: 14px;
    line-height: 23px;
    text-align: center;
  }
  .brand {
    left: 0; top: 31px; width: 92px; height: 84px;
    background: var(--white);
    border-radius: 0 6px 6px 0;
    display: flex; flex-direction: column; align-items: center; justify-content: center; gap: 5px;
  }
  .brand-dot { width: 16px; height: 16px; border-radius: 50%; background: var(--teal); }
  .brand-name { font-size: 15px; font-weight: 700; color: var(--teal); line-height: 1.05; text-align: center; }

  .offer-get {
    left: 104px;
    font-size: 34px; font-weight: 900; color: var(--red);
    transform: rotate(-90deg); transform-origin: left top;
    top: 104px; line-height: 1;
  }
  .offer-figure {
    left: 147px; top: 22px;
    font-size: 80px; font-weight: 900; color: var(--white);
    line-height: 1; letter-spacing: -2px;
  }
  .offer-figure small { font-size: 46px; letter-spacing: 0; }
  .offer-terms {
    left: 118px; top: 108px;
    font-size: 13px; color: var(--navy); white-space: nowrap;
  }

  .exclusive {
    background: var(--red);
    color: var(--white);
    font-family: "Roboto Condensed", Arial, sans-serif;
    font-weight: 700;
    text-align: center;
    display: flex; align-items: center; justify-content: center;
  }
  .flyer--a .exclusive { left: 0; top: 136px; width: 170px; height: 140px; font-size: 18px; line-height: 1.2; }
  .flyer--b .exclusive { left: 13px; top: 256px; width: 282px; height: 96px; font-size: 21px; line-height: 1.2; border-radius: 10px; border: 3px solid var(--white); }

  .photo { border: 2px solid var(--white); }
  .photo--dress { background: linear-gradient(160deg, #f4f1ef 0%, #e6d7d6 55%, #c96e6e 100%); }
  .photo--baby { background: radial-gradient(circle at 50% 40%, #f2b6a9 0%, #e0457a 55%, #c23166 100%); }
  .photo--garden { background: linear-gradient(170deg, #4a5a64 0%, #6d7a5c 45%, #46763a 75%, #2f5a2a 100%); }
  .flyer--a .photo--dress { left: 176px; top: 130px; width: 54px; height: 76px; }
  .flyer--a .photo--baby { left: 176px; top: 212px; width: 54px; height: 76px; }
  .flyer--a .photo--garden { left: 232px; top: 130px; width: 218px; height: 162px; border-right: 0; }
  .flyer--b .photo { border-radius: 50%; border: 4px solid var(--white); }
  .flyer--b .photo--baby { left: 13px; top: 136px; width: 118px; height: 118px; }
  .flyer--b .photo--dress { left: 123px; top: 136px; width: 116px; height: 116px; }
  .flyer--b .photo--garden { left: 223px; top: 116px; width: 236px; height: 236px; }

  .toy {
    width: 66px; height: 48px;
    background: var(--white);
    border: 2px solid #9a8fc0;
    border-radius: 4px;
    padding: 7px;
  }
  .toy span { display: block; width: 100%; height: 100%; border-radius: 6px; }
  .toy--horse span { background: linear-gradient(135deg, #e64a8c, #6a5bc0, #35b3d9); }
  .toy--snake span { background: linear-gradient(90deg, #e73a3a, #f6d02a, #3fb34f, #2f7ad1); }
  .toy--worm span { background: linear-gradient(90deg, #2f7ad1, #3fb34f, #f6d02a, #e73a3a); border-radius: 14px; height: 60%; margin-top: 20%; }
  .toy--bus span { background: linear-gradient(180deg, #d8262d, #b51d24); }
  .toy--plane span { background: radial-gradient(circle, #34bcd0 40%, #1f95aa 100%); border-radius: 50%; }
  .toy--car span { background: radial-gradient(ellipse at 50% 60%, #e3262c 45%, #a8161b 100%); border-radius: 50% 50% 30% 30%; }

  .jars {
    border-radius: 4px;
    background: linear-gradient(90deg, #efe3c6 0%, #d9c39a 25%, #e8ddc5 50%, #c9d8d2 75%, #eadcc0 100%);
  }
  .flyer--a .jars { left: 263px; top: 306px; width: 180px; height: 32px; }
  .flyer--b .jars { left: 263px; top: 372px; width: 160px; height: 32px; }

  .prize {
    background: var(--red);
    border-radius: 8px;
    border: 2px solid var(--white);
    color: var(--white);
    text-align: center;
    padding-top: 6px;
  }
  .flyer--a .prize { left: 242px; top: 336px; width: 204px; height: 73px; }
  .flyer--b .prize { left: 244px; top: 406px; width: 200px; height: 70px; }
  .prize-title { font-family: "Roboto Condensed", Arial, sans-serif; font-weight: 700; font-size: 20px; line-height: 1.1; }
  .prize-note { font-size: 11px; line-height: 1.25; }

  .winner {
    left: 0; width: 100%;
    text-align: center;
    font-family: "Roboto Condensed", Arial, sans-serif;
    color: var(--ink);
    font-size: 21px;
  }
  .winner b { font-weight: 700; }
  .flyer--a .winner { top: 424px; }
  .flyer--b .winner { top: 494px; }

  .launch {
    background: var(--purple);
    border: 3px solid var(--white);
    border-radius: 8px;
    color: var(--white);
    text-align: center;
  }
  .flyer--a .launch { left: 62px; top: 460px; width: 324px; height: 88px; padding-top: 10px; }
  .flyer--b .launch { left: 96px; top: 520px; width: 258px; height: 70px; padding-top: 6px; }
  .launch-lead { font-size: 13px; white-space: nowrap; }
  .flyer--b .launch-lead { font-size: 10.5px; line-height: 14px; }
  .launch-shop { font-weight: 900; line-height: 1.15; }
  .flyer--a .launch-shop { font-size: 34px; }
  .flyer--b .launch-shop { font-size: 26px; }

  .register {
    background: var(--yellow);
    color: var(--ink);
    font-weight: 900;
    text-align: center;
    border-radius: 3px;
  }
  .flyer--a .register { left: 122px; top: 550px; width: 204px; height: 32px; font-size: 21px; line-height: 32px; }
  .flyer--b .register { left: 141px; top: 580px; width: 168px; height: 24px; font-size: 17px; line-height: 24px; }

  .draw-note { left: 0; width: 100%; text-align: center; font-size: 11.5px; color: var(--navy); }
  .flyer--a .draw-note { top: 604px; }
  .flyer--b .draw-note { top: 614px; }

  .fine-print {
    font-size: 8px; color: var(--navy);
    transform: rotate(-90deg); transform-origin: left top;
    white-space: nowrap;
  }
  .flyer--a .fine-print { left: 22px; top: 548px; }
  .flyer--b .fine-print { left: 18px; top: 606px; }
</style>
</head>
<body>

<section class="flyer flyer--a" aria-label="Mailer option one">
  <div class="header-band"></div>
  <div class="body-field"></div>

  <p class="member-tag">if they register as members they will</p>
  <div class="brand"><span class="brand-dot"></span><span class="brand-name">Soft<br>Sprout</span></div>
  <span class="offer-get">get</span>
  <p class="offer-figure">20%<small>off</small></p>
  <p class="offer-terms">their first purchase and a 10% thereafter as members.</p>

  <p class="exclusive">clothes are new to<br>Singapore<br>and we have<br>exclusivity<br>with the brands*</p>
  <div class="photo photo--dress" role="img" aria-label="Patterned baby sleeping bag"></div>
  <div class="photo photo--baby" role="img" aria-label="Baby in a pink hat and outfit"></div>
  <div class="photo photo--garden" role="img" aria-label="Children playing with a watering can in a garden"></div>

  <div class="toy toy--horse" style="left:8px;top:304px" role="img" aria-label="Toy horse"><span></span></div>
  <div class="toy toy--snake" style="left:86px;top:304px" role="img" aria-label="Toy caterpillar"><span></span></div>
  <div class="toy toy--worm" style="left:164px;top:304px" role="img" aria-label="Stacking toy"><span></span></div>
  <div class="toy toy--bus" style="left:8px;top:364px" role="img" aria-label="Toy bus"><span></span></div>
  <div class="toy toy--plane" style="left:86px;top:364px" role="img" aria-label="Toy plane"><span></span></div>
  <div class="toy toy--car" style="left:164px;top:364px" role="img" aria-label="Toy car"><span></span></div>

  <div class="jars" role="img" aria-label="Toiletry jars from the Tiny Amber Meadows range"></div>
  <div class="prize">
    <p class="prize-title">5 Consolation Prizes</p>
    <p class="prize-note">that will be from the<br>Tiny Amber Meadows toiletry range.</p>
  </div>

  <p class="winner"><b>Winner gets $500 worth</b> of goods (at RRP)</p>

  <div class="launch">
    <p class="launch-lead">this is in conjunction with the launch of our new</p>
    <p class="launch-shop">on-line shop.</p>
  </div>
  <p class="register">Register Now</p>
  <p class="fine-print">*terms and conditions apply</p>
  <p class="draw-note">They will also be in a lucky draw contest for a $500 voucher to use at our wen site.</p>
</section>

<section class="flyer flyer--b" aria-label="Mailer option two">
  <div class="header-band"></div>
  <svg class="header-curve" viewBox="0 0 450 60" preserveAspectRatio="none" aria-hidden="true">
    <path d="M0 56 L0 0 L450 0 L450 30 Q260 40 0 56 Z" fill="var(--cyan)"/>
    <path d="M250 46 Q350 36 450 32 L450 38 Q350 42 250 46 Z" fill="var(--cyan-deep)"/>
  </svg>
  <div class="body-field"></div>

  <p class="member-tag">if they register as members they will</p>
  <div class="brand"><span class="brand-dot"></span><span class="brand-name">Soft<br>Sprout</span></div>
  <span class="offer-get">get</span>
  <p class="offer-figure">20%<small>off</small></p>
  <p class="offer-terms">their first purchase and a 10% thereafter as members.</p>

  <div class="photo photo--garden" role="img" aria-label="Children playing with a watering can in a garden"></div>
  <div class="photo photo--baby" role="img" aria-label="Baby in a pink hat and outfit"></div>
  <div class="photo photo--dress" role="img" aria-label="Patterned baby sleeping bag"></div>
  <p class="exclusive">clothes are new to<br>Singapore and we have<br>exclusivity with the brands*</p>

  <div class="toy toy--horse" style="left:10px;top:367px" role="img" aria-label="Toy horse"><span></span></div>
  <div class="toy toy--snake" style="left:88px;top:367px" role="img" aria-label="Toy caterpillar"><span></span></div>
  <div class="toy toy--worm" style="left:166px;top:367px" role="img" aria-label="Stacking toy"><span></span></div>
  <div class="toy toy--bus" style="left:10px;top:427px" role="img" aria-label="Toy bus"><span></span></div>
  <div class="toy toy--plane" style="left:88px;top:427px" role="img" aria-label="Toy plane"><span></span></div>
  <div class="toy toy--car" style="left:166px;top:427px" role="img" aria-label="Toy car"><span></span></div>

  <div class="jars" role="img" aria-label="Toiletry jars from the Tiny Amber Meadows range"></div>
  <div class="prize">
    <p class="prize-title">5 Consolation Prizes</p>
    <p class="prize-note">that will be from the<br>Tiny Amber Meadows toiletry range.</p>
  </div>

  <p class="winner"><b>Winner gets $500 worth</b> of goods (at RRP)</p>

  <div class="launch">
    <p class="launch-lead">this is in conjunction with the launch of our new</p>
    <p class="launch-shop">on-line shop.</p>
  </div>
  <p class="register">Register Now</p>
  <p class="fine-print">*terms and conditions apply</p>
  <p class="draw-note">They will also be in a lucky draw contest for a $500 voucher to use at our wen site.</p>
</section>

</body>
</html>
```